South Gulf Cove Post Card advertising my new real estate website

I want to send a postcard to owners in the community of South Gulf Cove Advertising my new website. www.tarrowbendlistings.com This is a page on www.danawhitcomberealty.com I would like to use the home page picture on www.tarrowbendlistings.com as the main big picture and keep the search field on it. on the front of the postcard with my contact info and logo along the bottom of the postcard. On the back of the card I would like to have one side address what is available on the website and include the "how much is your home worth" widget on my webdite along with the Items and I like the check marks for Interactive Map Search, Free Daily Email Updates, Automated Home Searches, Favorite Properties, And Much More. You should be able to find all my logos and contact information on my website or attached below

Target Market(s)

Lot and Homeowners in the community of South Gulf Cove

Industry/Entity Type

Real Estate Agent

Font styles to use
Serif

Colors
0255a3
0592cd
fbed22

Requirements
Must have
• I am a real estate agent - I don't want the front to be too busy just the main page picture and my logos and contact information at the bottom. Also highlighting the www.tarrowbendlistings.com web address prominent on big picture
• use the www.danawhitcomberealty.com web address with contact info at bottom
Nice to have
• This will be mailed so one side of the back of the card should have what I mentioned above regrading home worth widget and check marked features and the other side should be left for mailing purposes. Name logo and return address should be there and for this portion only use the Hemlock Farrow or HF logo as the name of my company and return address will be to Hemlock Farrow Realty

```html
<!DOCTYPE html>
<html lang="en">
<head>
<meta charset="utf-8">
<title>Dana Whitcombe – South Gulf Cove Postcard</title>
<link href="https://fonts.googleapis.com/css2?family=Arimo:ital,wght@0,400;0,700;1,400&display=swap" rel="stylesheet">
<style>
:root{
  --bg:#e9e6e2;
  --card:#ffffff;
  --navy:#3d5a94;
  --brand-blue:#0255a3;
  --sky:#0592cd;
  --orange:#e8842a;
  --ink:#111111;
  --muted:#444444;
  --panel:rgba(255,255,255,.55);
  --field:#ffffff;
  --btn:#3b64a8;
  --widget:rgba(50,50,50,.85);
  --submit:#5cb85c;
  --mail:#ebe9ea;
}
*{box-sizing:border-box;margin:0;padding:0}
html,body{width:1200px;height:1000px;overflow:hidden}
body{background:var(--bg);font-family:"Arimo",Arial,sans-serif;position:relative;color:var(--ink)}

.postcard{position:absolute;background:var(--card);overflow:hidden;box-shadow:0 6px 14px rgba(0,0,0,.25)}
.front{left:40px;top:32px;width:707px;height:453px}
.back{left:457px;top:510px;width:706px;height:454px}

/* front */
.hero-photo{position:absolute;left:0;top:0;width:707px;height:360px;
  background:linear-gradient(180deg,#4f80b8 0%,#7f9fbe 18%,#6f8a8e 40%,#5e7a66 65%,#3f5a72 85%,#2c4a6e 100%)}
.hero-title{position:absolute;left:53px;top:26px;color:#fff;font-size:27px;font-weight:700;letter-spacing:-.2px;text-shadow:0 1px 3px rgba(0,0,0,.35)}
.search-panel{position:absolute;left:53px;top:69px;width:312px;height:236px;background:var(--panel);border-radius:5px}
.field-label{position:absolute;font-size:9.5px;font-weight:700;color:#222}
.select{position:absolute;height:20px;background:var(--field);border:1px solid #bbb;border-radius:2px;font-size:9px;color:#222;padding:5px 0 0 6px}
.select::after{content:"▼";position:absolute;right:0;top:0;width:16px;height:18px;border-left:1px solid #ccc;font-size:8px;text-align:center;line-height:18px}
.to{position:absolute;left:148px;top:73px;font-size:10px;font-weight:700;color:#222}
.checks{position:absolute;left:11px;top:158px;display:flex;gap:12px;font-size:9px;color:#222}
.checks span{display:flex;align-items:center;gap:3px}
.box{width:8px;height:8px;border:1px solid #666;background:#fff;display:inline-block;position:relative}
.box.on::after{content:"";position:absolute;left:2px;top:-1px;width:3px;height:6px;border:solid var(--navy);border-width:0 2px 2px 0;transform:rotate(40deg)}
.search-btn{position:absolute;left:11px;top:189px;width:109px;height:34px;background:var(--btn);color:#fff;border-radius:3px;font-size:14px;text-align:center;line-height:34px}
.advanced-link{position:absolute;left:141px;top:198px;font-size:11px;color:var(--navy);border-bottom:2px solid var(--navy);padding-bottom:1px}
.hero-band{position:absolute;left:0;top:360px;width:707px;height:4px;background:var(--navy)}
.brand-name{position:absolute;font-weight:700;color:var(--navy);letter-spacing:1px;display:flex;align-items:center;gap:10px;white-space:nowrap}
.brand-name i{display:inline-block;background:var(--orange)}
.front .brand-name{left:52px;top:396px;font-size:22px}
.front .brand-name i{width:22px;height:22px}
.agent-contact{position:absolute;left:432px;top:372px;font-size:9px;color:#222;line-height:14px}
.agent-contact strong{display:block;font-size:11px;line-height:14px;color:#111}
.contact-line{display:flex;align-items:center;gap:4px;white-space:nowrap}
.contact-line svg{width:8px;height:8px;flex:none}
.contact-line .gap{width:8px}

/* back */
.house-photo{position:absolute;left:0;top:0;width:470px;height:330px;
  background:radial-gradient(ellipse at 35% 35%,#b9c2be 0%,#d6dcd8 40%,rgba(255,255,255,0) 75%)}
.value-widget{position:absolute;left:38px;top:46px;width:372px;height:132px;background:var(--widget);border-radius:8px;color:#fff;text-align:center}
.value-widget h2{font-weight:400;font-size:22px;margin-top:17px}
.value-widget p{font-size:22px;margin-top:10px}
.value-widget p em{text-decoration:underline}
.address-input{position:absolute;left:9px;top:94px;width:237px;height:28px;background:#fff;border-radius:4px 0 0 4px}
.unit-input{position:absolute;left:246px;top:94px;width:58px;height:28px;background:#fff;border-left:1px solid #ccc;color:#444;font-size:9px;text-align:left;padding:9px 0 0 4px}
.submit-btn{position:absolute;left:304px;top:94px;width:59px;height:28px;background:var(--submit);border-radius:0 4px 4px 0;font-size:10px;line-height:28px;color:#fff}
.feature-list{position:absolute;font-size:13px;font-weight:700;color:#111;display:flex;align-items:center;gap:1px;white-space:nowrap}
.feature-list svg{width:13px;height:12px}
.back .brand-name{left:100px;top:290px;font-size:23px}
.back .brand-name i{width:24px;height:24px}
.back-contact{position:absolute;left:0;width:460px;text-align:center;font-size:9px;color:#222}
.back-contact .contact-line{justify-content:center;gap:4px}
.partner-name{position:absolute;left:50px;top:395px;font-size:11px;font-weight:700;color:#111;display:flex;align-items:center;gap:5px;white-space:nowrap}
.partner-name i{width:18px;height:18px;background:#111;display:inline-block}
.partner-badge{position:absolute;left:186px;top:384px;width:98px;height:36px;border:2px solid #111;border-radius:3px}
.stamp-box{position:absolute;left:588px;top:12px;width:103px;height:103px;background:var(--mail)}
.mailing-area{position:absolute;background:var(--mail)}
.mailing-area.upper{left:463px;top:193px;width:243px;height:261px}
.mailing-area.lower{left:300px;top:390px;width:163px;height:64px}
</style>
</head>
<body>

<section class="postcard front">
  <div class="hero-photo" role="img" aria-label="Aerial photograph of the South Gulf Cove canal community and the bay"></div>
  <h1 class="hero-title">South Gulf Cove Real Estate Search</h1>
  <div class="search-panel">
    <span class="field-label" style="left:11px;top:13px">City</span>
    <div class="select" style="left:11px;top:25px;width:134px">Port Charlotte</div>
    <span class="field-label" style="left:167px;top:13px">Subdivision</span>
    <div class="select" style="left:167px;top:25px;width:134px">All Subdivisions</div>
    <span class="field-label" style="left:11px;top:56px">Price</span>
    <div class="select" style="left:11px;top:68px;width:108px">No Limit</div>
    <span class="to">TO</span>
    <div class="select" style="left:193px;top:68px;width:108px">No Limit</div>
    <span class="field-label" style="left:11px;top:99px">Beds</span>
    <div class="select" style="left:11px;top:111px;width:56px">Any</div>
    <span class="field-label" style="left:89px;top:99px">Baths</span>
    <div class="select" style="left:89px;top:111px;width:56px">Any</div>
    <span class="field-label" style="left:11px;top:141px">Property Type</span>
    <div class="checks">
      <span><i class="box on"></i>Home</span>
      <span><i class="box on"></i>Condo</span>
      <span><i class="box"></i>Land</span>
      <span><i class="box"></i>Multi-Res</span>
    </div>
    <div class="search-btn">Search</div>
    <span class="advanced-link">Advanced Search</span>
  </div>
  <div class="hero-band"></div>

  <div class="brand-name"><i></i>DANA WHITCOMBE</div>

  <div class="agent-contact">
    <strong>Dana Whitcombe</strong>
    <strong>Hemlock Farrow Realty</strong>
    <div class="contact-line" style="margin-top:3px">
      <svg viewBox="0 0 10 10"><path d="M5 1 1 5h1.5v4h2V6.5h1V9h2V5H9z" fill="var(--orange)"/></svg>
      718 W. Harbor St. PO Box 312 Cedar Point, FL 33900
    </div>
    <div class="contact-line">
      <svg viewBox="0 0 10 10"><circle cx="5" cy="5" r="4.3" fill="none" stroke="var(--orange)"/><path d="M3.5 3c.3 1.8 1.4 3.2 3 3.8" stroke="var(--orange)" fill="none"/></svg>
      (941) 555-0147 <span class="gap"></span>
      <svg viewBox="0 0 10 10"><rect x="1" y="2.5" width="8" height="5.5" fill="none" stroke="var(--orange)"/><path d="M1 2.5 5 6l4-3.5" fill="none" stroke="var(--orange)"/></svg>
      dana@danawhitcomberealty.com
    </div>
    <div class="contact-line">
      <svg viewBox="0 0 10 10"><circle cx="5" cy="5" r="4.3" fill="none" stroke="var(--orange)"/><path d="M1 5h8M5 .7c-2 2.5-2 6 0 8.6M5 .7c2 2.5 2 6 0 8.6" fill="none" stroke="var(--orange)" stroke-width=".7"/></svg>
      www.danawhitcomberealty.com
    </div>
  </div>
</section>

<section class="postcard back">
  <div class="house-photo" role="img" aria-label="Faded photograph of a suburban home and street"></div>
  <div class="stamp-box"></div>
  <div class="mailing-area upper"></div>
  <div class="mailing-area lower"></div>

  <div class="value-widget">
    <h2>How much is your home worth?</h2>
    <p>...get <em>instant</em> property value now!</p>
    <div class="address-input"></div>
    <div class="unit-input">Unit#</div>
    <div class="submit-btn">Submit</div>
  </div>

  <div class="feature-list" style="left:35px;top:194px"><svg viewBox="0 0 13 12"><path d="M1 6.5 4.5 10 12 1.5" fill="none" stroke="var(--navy)" stroke-width="2.2"/></svg>Free Daily Email Updates</div>
  <div class="feature-list" style="left:226px;top:194px"><svg viewBox="0 0 13 12"><path d="M1 6.5 4.5 10 12 1.5" fill="none" stroke="var(--navy)" stroke-width="2.2"/></svg>Automated Home Searches</div>
  <div class="feature-list" style="left:35px;top:213px"><svg viewBox="0 0 13 12"><path d="M1 6.5 4.5 10 12 1.5" fill="none" stroke="var(--navy)" stroke-width="2.2"/></svg>Favorite Properties</div>
  <div class="feature-list" style="left:226px;top:213px"><svg viewBox="0 0 13 12"><path d="M1 6.5 4.5 10 12 1.5" fill="none" stroke="var(--navy)" stroke-width="2.2"/></svg>Email Updates</div>
  <div class="feature-list" style="left:166px;top:234px"><svg viewBox="0 0 13 12"><path d="M1 6.5 4.5 10 12 1.5" fill="none" stroke="var(--navy)" stroke-width="2.2"/></svg>And Much More!</div>

  <div class="brand-name"><i></i>DANA WHITCOMBE</div>

  <div class="back-contact" style="top:344px">
    <div class="contact-line">
      <svg viewBox="0 0 10 10"><path d="M5 1 1 5h1.5v4h2V6.5h1V9h2V5H9z" fill="var(--orange)"/></svg>
      718 W. Harbor St. PO Box 312 Cedar Point, FL 33900
    </div>
  </div>
  <div class="back-contact" style="top:358px">
    <div class="contact-line">
      <svg viewBox="0 0 10 10"><circle cx="5" cy="5" r="4.3" fill="none" stroke="var(--orange)"/><path d="M3.5 3c.3 1.8 1.4 3.2 3 3.8" stroke="var(--orange)" fill="none"/></svg>
      (941) 555-0147 <span class="gap"></span>
      <svg viewBox="0 0 10 10"><rect x="1" y="2.5" width="8" height="5.5" fill="none" stroke="var(--orange)"/><path d="M1 2.5 5 6l4-3.5" fill="none" stroke="var(--orange)"/></svg>
      dana@danawhitcomberealty.com <span class="gap"></span>
      <svg viewBox="0 0 10 10"><circle cx="5" cy="5" r="4.3" fill="none" stroke="var(--orange)"/><path d="M1 5h8M5 .7c-2 2.5-2 6 0 8.6M5 .7c2 2.5 2 6 0 8.6" fill="none" stroke="var(--orange)" stroke-width=".7"/></svg>
      www.danawhitcomberealty.com
    </div>
  </div>

  <div class="partner-name"><i></i>Hemlock Farrow</div>
  <div class="partner-badge"></div>
</section>

</body>
</html>
```